Music Business Adviser Needs a Book Cover Design

I need a cover design for my new book called 'The Stage Performer: A Working Handbook for Launching Your Trade'. I am an accountant and tax lawyer specialising in advising international music artists. This book is designed to help music artists and bands navigate through the business world. I would like to see designs that would appeal to young artists, the book needs to be bold and stand out from the crowd, for example it will attract people on Bookvale through its enticing cover.

I am open to you providing creative input on the design, although I like the colour green and think this would perhaps communicate subtly financial safety and growth. The cover should clearly communicate the book is for people in the music industry.

Target Market(s)

Males and females aged between 16 and 30; their hobbies and interest are music; they perform and record music; all genres of music

Industry/Entity Type

Lawyer

Font styles to use
Sans Serif

Requirements
Must have
• Must have the title clearly stated: 'The Stage Performer: A Working Handbook for Launching Your Trade'. It must also have my name as author on the front: 'Gareth L. Quinby'
Nice to have
• I have uploaded an image of the type of artwork, that should be on the book. I like this style - so please keep it simple, not an over complicated design.
Should not have
• Photographs of bands or musicians

```html
<!DOCTYPE html>
<html lang="en">
<head>
<meta charset="utf-8">
<title>The Stage Performer – Book Cover</title>
<link rel="stylesheet" href="https://fonts.googleapis.com/css2?family=Roboto+Condensed:wght@300;400;700&display=swap">
<style>
  :root {
    --forest: #1f4a12;
    --forest-deep: #153a0b;
    --leaf: #80c343;
    --gold: #f6c216;
    --gold-soft: #f3d64f;
    --signal-red: #d2232a;
    --paper: #ffffff;
    --font: "Roboto Condensed", Arial Narrow, sans-serif;
  }
  * { margin: 0; padding: 0; box-sizing: border-box; }
  html, body { width: 1200px; height: 885px; overflow: hidden; background: var(--forest); }
  .cover { position: relative; width: 1200px; height: 885px; background: var(--forest); font-family: var(--font); overflow: hidden; }

  /* back cover */
  .back-stripe { position: absolute; left: 83px; width: 33px; }
  .back-stripe--leaf { top: 0; height: 523px; background: var(--leaf); }
  .back-stripe--gold { top: 523px; height: 210px; background: var(--gold); }
  .back-motif { position: absolute; left: 0; top: 470px; width: 240px; height: 415px;
    background: radial-gradient(ellipse at 40% 55%, rgba(110,160,80,0.28), rgba(31,74,18,0) 70%); }

  .back-title { position: absolute; right: calc(1200px - 508px); top: 94px; color: var(--gold); font-size: 31px; font-weight: 400; white-space: nowrap; }
  .back-title strong, .front-title strong { font-weight: 700; }
  .back-rule { position: absolute; left: 359px; top: 136px; width: 228px; height: 2px; background: var(--signal-red); }
  .back-subtitle { position: absolute; right: calc(1200px - 507px); top: 143px; color: var(--gold-soft); font-size: 16.5px; font-weight: 300; line-height: 22px; text-align: right; }
  .back-author { position: absolute; left: 262px; top: 199px; color: var(--paper); font-size: 17.5px; font-weight: 700; }
  .blurb { position: absolute; left: 192px; top: 252px; width: 312px; color: var(--paper); font-size: 14px; font-weight: 400; line-height: 24.2px; text-align: justify; }
  .blurb p + p { margin-top: 24px; }
  .code-panel { position: absolute; left: 372px; top: 740px; width: 192px; height: 116px; background: var(--paper); }

  /* spine */
  .spine { position: absolute; left: 587px; top: 0; width: 26px; height: 885px; background: var(--gold); }
  .spine-text { position: absolute; left: 0; width: 26px; writing-mode: vertical-rl; transform: rotate(180deg);
    color: var(--forest); font-size: 17px; font-weight: 700; line-height: 26px; white-space: nowrap; text-align: center; }
  .spine-author { top: 58px; height: 136px; border-top: 2px solid var(--signal-red); }
  .spine-title { top: 300px; height: 530px; font-size: 16.5px; }

  /* front cover */
  .front-band { position: absolute; top: 0; left: 613px; width: 506px; height: 115px; background: var(--leaf); }
  .front-corner { position: absolute; top: 0; left: 1119px; width: 81px; height: 115px; background: var(--gold); }
  .front-title { position: absolute; right: calc(1200px - 1116px); top: 156px; color: var(--gold); font-size: 60px; font-weight: 400; white-space: nowrap; letter-spacing: -0.5px; }
  .front-rule { position: absolute; left: 846px; top: 234px; width: 354px; height: 3px; background: var(--signal-red); }
  .front-subtitle { position: absolute; right: calc(1200px - 1114px); top: 248px; color: var(--gold-soft); font-size: 30px; font-weight: 300; line-height: 39px; text-align: right; }
  .artwork { position: absolute; left: 644px; top: 460px; width: 556px; height: 425px;
    background: radial-gradient(ellipse at 45% 60%, var(--forest-deep) 0%, rgba(21,58,11,0.6) 45%, rgba(31,74,18,0) 75%); }
  .front-author { position: absolute; right: calc(1200px - 1114px); top: 750px; color: var(--paper); font-size: 31px; font-weight: 700; white-space: nowrap; }
  .front-tab { position: absolute; left: 1128px; top: 756px; width: 72px; height: 31px; background: var(--gold); }
</style>
</head>
<body>
<main class="cover">
  <section class="back">
    <div class="back-stripe back-stripe--leaf"></div>
    <div class="back-stripe back-stripe--gold"></div>
    <div class="back-motif" role="img" aria-label="Faint scattered music notes decoration"></div>
    <h2 class="back-title">The Stage <strong>Performer</strong></h2>
    <div class="back-rule"></div>
    <p class="back-subtitle">a working handbook<br>for launching<br>your trade</p>
    <p class="back-author">Gareth L. Quinby</p>
    <div class="blurb">
      <p>The music industry is shapeshifting. Music artists must work harder than ever to make a career of their creative mastery.</p>
      <p>As an artist you are not in a typical profession but you can be big business. A good business mindset starts with ensuring you understand that you are a business and that you will need the right team on board to help you navigate the legal complexities of the business world.</p>
      <p>Whilst you may have a first rate attack in terms of your manager and record label, success won’t be guaranteed unless you have a first rate line of defense to help protect your earnings. This book provides an easy-to-understand overview of setting up in business for the first time, some practical tips on getting started, as well as a discussion of the business challenges you’ll face along your journey to becoming and international superstar.</p>
    </div>
    <div class="code-panel"></div>
  </section>

  <section class="spine">
    <div class="spine-text spine-title">The Stage Performer - a working handbook for launching your trade</div>
    <div class="spine-text spine-author">Gareth L. Quinby</div>
  </section>

  <section class="front">
    <div class="front-band"></div>
    <div class="front-corner"></div>
    <h1 class="front-title">The Stage <strong>Performer</strong></h1>
    <div class="front-rule"></div>
    <p class="front-subtitle">a working handbook<br>for launching<br>your trade</p>
    <div class="artwork" role="img" aria-label="Silhouette of a head in profile with music notes flowing out like hair"></div>
    <p class="front-author">Gareth L. Quinby</p>
    <div class="front-tab"></div>
  </section>
</main>
</body>
</html>
```